business card design

i would like business cards designed. My business provides trade qualified personnel to the mining industry to work on heavy mobile equipment.
please put a excavator(digger) in the background in one design and have one design without so i can compare the difference.
also add info:
my logo(attached) and "mobile equipment repair and maintenance"
name: Derek Holloway
address: 57 Tarrowby RD Carmel Perth WA.
mobile: 0438120957
email: derek@ironvalemx.com

```html
<!DOCTYPE html>
<html lang="en">
<head>
<meta charset="utf-8">
<title>Ironvale Maintenance Services – Business Cards</title>
<link rel="stylesheet" href="https://fonts.googleapis.com/css2?family=Lato:wght@400;700;900&display=swap">
<style>
  :root {
    --backdrop: #b3b3b3;
    --navy: #061f40;
    --navy-ink: #0b2145;
    --accent-blue: #4a75c8;
    --white: #ffffff;
    --text-dark: #111111;
  }
  * { box-sizing: border-box; margin: 0; padding: 0; }
  html, body {
    width: 1200px; height: 1200px; overflow: hidden;
    background: var(--backdrop);
    font-family: "Lato", Arial, sans-serif;
  }
  .canvas { position: relative; width: 1200px; height: 1200px; }

  .card {
    position: absolute;
    box-shadow: 2px 2px 3px rgba(0,0,0,0.35);
    overflow: hidden;
  }
  .card--front { left: 233px; top: 158px; width: 742px; height: 424px; background: var(--navy); }
  .card--back  { left: 235px; top: 628px; width: 737px; height: 422px; background: var(--white); }

  .brand { position: absolute; white-space: nowrap; }
  .brand__name {
    display: block;
    font-weight: 900;
    font-size: 50px;
    line-height: 1;
    letter-spacing: 12px;
  }
  .brand__sub {
    display: block;
    margin-top: 5px;
    margin-left: 37px;
    font-weight: 700;
    font-size: 12px;
    letter-spacing: 2.3px;
    color: var(--accent-blue);
  }
  .card--front .brand { left: 25px; top: 68px; }
  .card--front .brand__name { color: var(--white); }
  .card--back .brand { left: 26px; top: 174px; }
  .card--back .brand__name { color: var(--navy-ink); }

  .tagline {
    position: absolute;
    left: 25px; top: 360px;
    color: var(--white);
    font-size: 17px;
    font-weight: 400;
    white-space: nowrap;
  }

  .machine-photo {
    position: absolute;
    left: 456px; top: 38px;
    width: 252px; height: 344px;
    border-radius: 6px;
    background: linear-gradient(160deg, rgba(200,87,47,0.85) 0%, rgba(160,72,44,0.75) 45%, rgba(42,48,64,0.9) 100%);
  }

  .contact-name {
    position: absolute;
    right: 47px; top: 190px;
    font-weight: 700;
    font-size: 31px;
    color: var(--navy-ink);
    white-space: nowrap;
  }
  .contact-list {
    position: absolute;
    right: 27px; top: 258px;
    list-style: none;
    text-align: right;
  }
  .contact-list li {
    display: flex; justify-content: flex-end; align-items: center;
    height: 30px;
    font-size: 17px;
    color: var(--text-dark);
    white-space: nowrap;
  }
  .contact-list .icon {
    width: 19px; height: 19px; margin-left: 2px;
    border-radius: 50%;
    background: var(--navy-ink);
    display: inline-flex; align-items: center; justify-content: center;
  }
  .contact-list svg { width: 11px; height: 11px; fill: var(--white); }
</style>
</head>
<body>
<main class="canvas">

  <section class="card card--front">
    <div class="brand">
      <span class="brand__name">IRONVALE</span>
      <span class="brand__sub">MAINTENANCE SERVICES PTY LTD</span>
    </div>
    <div class="machine-photo" role="img" aria-label="Photo of an orange compact excavator with cab, boom and bucket"></div>
    <p class="tagline">“MOBILE EQUIPMENT REPAIR AND MAINTENANCE”</p>
  </section>

  <section class="card card--back">
    <div class="brand">
      <span class="brand__name">IRONVALE</span>
      <span class="brand__sub">MAINTENANCE SERVICES PTY LTD</span>
    </div>
    <h1 class="contact-name">Derek Holloway</h1>
    <ul class="contact-list">
      <li>0438120957<span class="icon"><svg viewBox="0 0 24 24"><path d="M6.6 10.8a15.2 15.2 0 0 0 6.6 6.6l2.2-2.2a1 1 0 0 1 1-.25 11.4 11.4 0 0 0 3.6.57 1 1 0 0 1 1 1V20a1 1 0 0 1-1 1A17 17 0 0 1 3 4a1 1 0 0 1 1-1h3.5a1 1 0 0 1 1 1c0 1.250.2 2.45.57 3.57a1 1 0 0 1-.25 1z"/></svg></span></li>
      <li>derek@ironvalemx.com<span class="icon"><svg viewBox="0 0 24 24"><path d="M2 11 22 2l-9 20-2.5-8.5z"/></svg></span></li>
      <li>57 Tarrowby RD Carmel Perth WA.<span class="icon"><svg viewBox="0 0 24 24"><path d="M12 2a7 7 0 0 0-7 7c0 5 7 13 7 13s7-8 7-13a7 7 0 0 0-7-7zm0 9.5A2.5 2.5 0 1 1 12 6.5a2.5 2.5 0 0 1 0 5z"/></svg></span></li>
    </ul>
  </section>

</main>
</body>
</html>
```